Business Card Design

Consultation for design, construction athletic facilities specializing in synthetic turf systems and all weather running track systems.
Motto "True Owner Representation"
New Company that we'd like to highlight the LOGO first and foremost with the colors of the background and font as primary colors of the card too if possible. I've also attached a typical larger project design layout that could be used in the background to highlight our design and construction specialty.
Website is something we want very noticeable for driving traffic.
Target Market(s)
Athletic Directors, Designers, Government and Military, Contractors
Industry/Entity Type
Construction
Contact Information for Business Card
Peter L. Vandrell CFB, CTB
48317 W 63rd Ave
Harlow Ridge, WA 99482
C +1 503.555.0147
O +1 808.555.0182
Peter@fieldlaneco.example
www.fieldlaneco.example

```html
<!DOCTYPE html>
<html lang="en">
<head>
<meta charset="utf-8">
<title>Fieldlane Co — Business Card</title>
<link rel="stylesheet" href="https://fonts.googleapis.com/css2?family=Arimo:wght@400;700&family=Open+Sans:wght@400&family=Tinos&display=swap">
<style>
  :root {
    --canvas: #e9e6e2;
    --card-black: #000000;
    --card-white: #ffffff;
    --ink-white: #ffffff;
    --accent-red: #e0262b;
    --accent-orange: #f0a23a;
    --brand-copper: #c98a4f;
    --brand-grey: #7a7a7a;
    --rule-grey: #bdbdbd;
    --ink-dark: #111111;
    --plan-light: #f4f4f4;
    --plan-mid: #e6e6e6;
    --footer-text: #f6b890;
  }
  * { margin: 0; padding: 0; box-sizing: border-box; }
  html, body { width: 1200px; height: 1200px; overflow: hidden; }
  body { background: var(--canvas); position: relative; }

  .card {
    position: absolute;
    top: 136px;
    width: 558px;
    height: 956px;
    overflow: hidden;
  }
  .card--front { left: 30px; background: var(--card-black); color: var(--ink-white); }
  .card--back { left: 618px; background: var(--card-white); }

  .brand {
    position: absolute;
    display: flex;
    align-items: center;
    gap: 18px;
    font-family: "Open Sans", Arial, sans-serif;
    font-weight: 400;
  }
  .brand__dot { width: 22px; height: 22px; border-radius: 50%; }
  .brand__name { font-size: 50px; letter-spacing: 4px; line-height: 1; white-space: nowrap; }
  .card--front .brand { left: 70px; top: 170px; }
  .card--front .brand__dot { background: var(--brand-copper); }
  .card--front .brand__name { color: var(--brand-copper); }
  .card--back .brand { left: 62px; top: 70px; }
  .card--back .brand__dot { background: var(--brand-grey); }
  .card--back .brand__name { color: var(--brand-grey); }

  .centered { position: absolute; left: 0; width: 100%; text-align: center; white-space: nowrap; }
  .person-name { top: 424px; font-family: "Arimo", Arial, sans-serif; font-size: 45px; }
  .credentials { top: 497px; font-family: "Arimo", Arial, sans-serif; font-size: 26px; color: var(--accent-red); }
  .rule { position: absolute; left: 36px; right: 36px; height: 2px; background: var(--rule-grey); }
  .rule--top { top: 558px; }
  .rule--bottom { top: 881px; }
  .contact { font-family: "Open Sans", Arial, sans-serif; font-size: 28px; line-height: 1; }
  .contact--addr1 { top: 598px; }
  .contact--addr2 { top: 647px; }
  .contact--cell { top: 721px; }
  .contact--office { top: 772px; }
  .contact--email { top: 823px; }
  .website { top: 902px; font-family: "Open Sans", Arial, sans-serif; font-size: 32px; color: var(--accent-orange); letter-spacing: 1px; }

  .site-plan {
    position: absolute;
    left: 0; top: 212px;
    width: 100%; height: 624px;
    background: radial-gradient(ellipse at 50% 55%, var(--plan-mid) 0%, var(--plan-light) 55%, var(--card-white) 100%);
  }
  .note {
    position: absolute;
    left: 40px; top: 268px;
    font-family: "Tinos", "Times New Roman", serif;
    font-size: 40px;
    color: var(--ink-dark);
  }
  .note-line { position: absolute; height: 2px; background: var(--ink-dark); }
  .note-line--label { left: 156px; width: 360px; top: 296px; }
  .note-line--end { left: 42px; width: 474px; top: 800px; }
  .footer-band { position: absolute; left: 0; top: 842px; width: 100%; height: 10px; background: var(--accent-red); }
  .footer {
    position: absolute; left: 0; top: 852px; width: 100%; height: 104px;
    background: var(--card-black);
    display: flex; align-items: center; justify-content: flex-end;
    padding: 0 20px;
  }
  .footer__website {
    font-family: "Arimo", Arial, sans-serif; font-weight: 700;
    font-size: 29px; color: var(--footer-text); letter-spacing: 0;
    white-space: nowrap;
  }
</style>
</head>
<body>
  <section class="card card--front" aria-label="Business card front">
    <div class="brand">
      <span class="brand__dot"></span>
      <span class="brand__name">Fieldlane Co</span>
    </div>
    <p class="centered person-name">Peter L. Vandrell</p>
    <p class="centered credentials">CFB, CTB</p>
    <div class="rule rule--top"></div>
    <p class="centered contact contact--addr1">48317 W 63rd Ave Harlow Ridge</p>
    <p class="centered contact contact--addr2">WA 99482</p>
    <p class="centered contact contact--cell">Cell : +1 503.555.0147</p>
    <p class="centered contact contact--office">Phone : +1 808.555.0182</p>
    <p class="centered contact contact--email">Peter@fieldlaneco.example</p>
    <div class="rule rule--bottom"></div>
    <p class="centered website">www.fieldlaneco.example</p>
  </section>

  <section class="card card--back" aria-label="Business card back">
    <div class="brand">
      <span class="brand__dot"></span>
      <span class="brand__name">Fieldlane Co</span>
    </div>
    <div class="site-plan" role="img" aria-label="Faint athletic facility site plan with running track, football field and ball fields"></div>
    <p class="note">Note</p>
    <div class="note-line note-line--label"></div>
    <div class="note-line note-line--end"></div>
    <div class="footer-band"></div>
    <div class="footer">
      <span class="footer__website">WWW.FIELDLANECO.EXAMPLE</span>
    </div>
  </section>
</body>
</html>
```